Ballet Sponsorship Ad

I need to have an ad created where my commercial real estate firm has a sponsorship ad for a ballet recital. The ad should include similar company branding to other ads and include a photo of my daughter congratulating her on the recital. The ad size MUST be 8.5" wide by 5.5" tall and needs to be sent in JPG and PDF format to me.

The contact information to include in the ad is:
274 W. Tollbridge Orchard Rd
Brantwood, VA 27415
(555) 463-5082
www.holtbankerre.com
desmond@holtbankerre.com

Real Estate

Requirements
Must have
• Photo of my daughter
• Company logo
• "Congratulations Lydia Banker"
• Company contact information

```html
<!DOCTYPE html>
<html lang="en">
<head>
<meta charset="utf-8">
<title>Holt-Banker Real Estate – Recital Sponsorship Ad</title>
<link rel="stylesheet" href="https://fonts.googleapis.com/css2?family=Pinyon+Script&family=Oswald:wght@600&family=Libre+Franklin:wght@400;500;700&display=swap">
<style>
  :root {
    --green: #1b4a1d;
    --green-deep: #123a15;
    --paper: #f4f4f3;
    --paper-edge: #e9e9e8;
    --ink: #333333;
    --white: #ffffff;
    --backdrop: #ececec;
  }
  * { margin: 0; padding: 0; box-sizing: border-box; }
  html, body { width: 1200px; height: 1200px; overflow: hidden; background: var(--backdrop); }
  .ad {
    position: absolute; left: 50px; top: 244px;
    width: 1100px; height: 712px;
    background: linear-gradient(180deg, var(--paper), var(--paper-edge));
    overflow: hidden;
    font-family: "Libre Franklin", Arial, sans-serif;
  }
  .ad__shapes { position: absolute; inset: 0; }
  .ad__photo {
    position: absolute; left: 700px; top: 23px; width: 400px; height: 482px;
    background:
      linear-gradient(90deg, var(--paper) 0%, rgba(244,244,243,0) 22%),
      linear-gradient(160deg, #d9d9d9 0%, #9b9b9b 45%, #6e6e6e 100%);
  }
  .greeting { position: absolute; left: 116px; top: 128px; width: 472px; height: 142px; text-align: center; }
  .greeting__rule { position: absolute; left: 0; width: 472px; height: 2px; background: var(--green); }
  .greeting__rule--top { top: 0; }
  .greeting__rule--bottom { top: 140px; }
  .greeting__word {
    position: absolute; left: 0; right: 0; top: 22px;
    font-family: "Pinyon Script", cursive; font-size: 72px; line-height: 1;
    color: var(--green);
  }
  .honoree {
    position: absolute; left: 116px; top: 310px; width: 472px; text-align: center;
    font-family: "Oswald", sans-serif; font-weight: 600; font-size: 76px; line-height: 1;
    color: var(--ink); letter-spacing: -0.5px;
  }
  .brand { position: absolute; left: 44px; top: 538px; display: flex; align-items: center; gap: 16px; color: var(--white); }
  .brand__mark { width: 76px; height: 76px; border-radius: 50%; background: var(--white); flex: none; }
  .brand__name { font-weight: 500; font-size: 34px; line-height: 1.05; }
  .brand__name span { display: block; font-size: 18px; letter-spacing: 5px; text-transform: uppercase; }
  .web { position: absolute; left: 46px; top: 654px; color: var(--white); font-weight: 700; font-size: 17px; }
  .contact { position: absolute; left: 485px; top: 520px; color: var(--white); font-size: 19px; line-height: 1.6; font-style: normal; }
  .contact__title { font-weight: 700; font-size: 20px; margin-bottom: 8px; }
  .contact__phone { display: flex; align-items: center; gap: 6px; margin-top: 6px; }
  .contact__phone svg { width: 18px; height: 18px; }
</style>
</head>
<body>
  <main class="ad">
    <div class="ad__photo" role="img" aria-label="Black and white photo of the young dancer in ballet pose by a window"></div>
    <svg class="ad__shapes" width="1100" height="712" viewBox="0 0 1100 712" aria-hidden="true">
      <path fill="var(--green)" d="M0 0 H1100 V23 H330 C230 23 150 30 90 48 C50 58 20 60 0 58 Z"/>
      <path fill="var(--green)" d="M0 480 C80 460 180 460 280 480 C330 492 380 505 440 505 H1100 V712 H0 Z"/>
    </svg>

    <section class="greeting">
      <div class="greeting__rule greeting__rule--top"></div>
      <div class="greeting__word">Congratulations</div>
      <div class="greeting__rule greeting__rule--bottom"></div>
    </section>
    <h1 class="honoree">LYDIA BANKER</h1>

    <div class="brand">
      <div class="brand__mark"></div>
      <div class="brand__name">Holt-Banker<span>Real Estate</span></div>
    </div>
    <div class="web">www.HoltBankerRE.com</div>

    <address class="contact">
      <div class="contact__title">Property Management Office</div>
      <div>274 W. Tollbridge Orchard Rd</div>
      <div>Brantwood, VA 27415</div>
      <div class="contact__phone">
        <svg viewBox="0 0 24 24" aria-hidden="true"><path fill="var(--white)" d="M6.6 10.8a15 15 0 0 0 6.6 6.6l2.2-2.2a1 1 0 0 1 1-.25 11.4 11.4 0 0 0 3.6.57 1 1 0 0 1 1 1V20a1 1 0 0 1-1 1A17 17 0 0 1 3 4a1 1 0 0 1 1-1h3.5a1 1 0 0 1 1 1c0 1.25.2 2.45.57 3.57a1 1 0 0 1-.25 1z"/></svg>
        (555) 463-5082
      </div>
      <div>desmond@holtbankerre.com</div>
    </address>
  </main>
</body>
</html>
```